Loftwise.com ;Take Yourself Up to the Next Level. More success, higher productivity, better health.

PLEASE READ IT CAREFULLY
I HAVE RECEIVED SOME FIRST DESIGNS AND I HAVE A FEELING THAT ALMOST NOBODY HAS READ THE BRIEFING CAREFULLY.

What I need actually is the design of the main visual
THE MAIN VISUAL MUST COMMUNICATE THE CONCEPT.
THIS WEBSITE IS ABOUT THE PERSONAL DEVELOPMENT.

The change of the main visual may be linked with other changes of other elements of the homepage, but this is the secondary task.

BACKGROUND
I have launched a blog on healthy productivity: loftwise.com

The problem is that the main visual does not communicate clearly what the website is about.

Currently I have a blog with advice on healthy productivity and a shop. In teh future I would like to offer stress management courses, fitness boot camps for executives, mindefulness courses, courses for healthy sleep and work-life balance.

The task is to develop the homepage which communicates the current positioning:

Loft Wise-
Take Yourself Up to the Next Level. More Success, Higher Productivity, Better Health.

The homepage should contain all the blocks of the current homepage. Actually the main task is to find the powerful design representation of the website positioning.
Updates

Low design quality

Target Market(s)

US executives, managers and entrepreneurs

Requirements
Must have
• You should keep in principle the current color code which is green, blue, grey
• The design project must contain all the current homepage elements like blog, testimonial, footnote etc

```html
<!DOCTYPE html>
<html lang="en">
<head>
<meta charset="utf-8">
<title>Loftwise – Take Yourself Up to the Next Level</title>
<link href="https://fonts.googleapis.com/css2?family=Lato:wght@400;700;900&display=swap" rel="stylesheet">
<style>
:root{
  --navy:#0f3350;
  --steel:#6f8fae;
  --steel-dark:#5f7f9d;
  --green:#63a944;
  --green-bright:#63b22a;
  --grey-card:#a3a3a3;
  --charcoal:#484848;
  --light:#efefef;
  --ink:#1d1d1d;
  --white:#ffffff;
  --amber:#fbb03b;
}
*{margin:0;padding:0;box-sizing:border-box}
html,body{width:1200px;height:3417px;overflow:hidden}
body{font-family:'Lato',sans-serif;color:var(--ink);background:var(--white);position:relative}
.abs{position:absolute}
.center{left:0;width:1200px;text-align:center}

/* header */
.header{top:0;left:0;width:1200px;height:103px;background:var(--white)}
.brand{left:75px;top:34px;display:flex;align-items:center;gap:10px;font-size:28px;letter-spacing:3px;color:#6a6a6a}
.brand .dot{width:14px;height:14px;border-radius:50%;background:var(--green)}
.nav{right:75px;top:43px;display:flex;gap:26px;font-size:13px}
.nav a{color:var(--ink);text-decoration:none;padding-bottom:6px}
.nav a.active{border-bottom:2px solid var(--green)}

/* hero */
.hero{top:103px;left:0;width:1200px;height:360px;background:linear-gradient(90deg,#ececec,#f6f6f6 60%,#ececec)}
.hero-portrait{left:170px;top:50px;width:370px;height:310px;border-radius:180px 180px 0 0;background:linear-gradient(180deg,#d9b9a6,#8a6f62 70%,#3f4650)}
.hero-growth{left:560px;top:110px;width:540px;height:250px;background:linear-gradient(180deg,rgba(251,176,59,0),rgba(251,176,59,.35) 60%,rgba(251,176,59,.55))}
.hero-title{top:240px;font-size:31px;font-weight:900}
.hero-sub{top:280px;font-size:20px;color:#333}
.btn-dark{left:504px;top:340px;width:192px;height:41px;background:var(--navy);color:var(--white);font-size:13px;font-weight:900;display:flex;align-items:center;justify-content:center;border-radius:3px}

/* promo band */
.promo{top:463px;left:0;width:1200px;height:120px;background:rgba(111,143,174,.95)}
.promo-col{top:22px}
.promo-col h3{font-size:20px;font-weight:700;color:var(--ink)}
.promo-col p{font-size:14px;margin-top:9px}
.promo-col a{display:block;font-size:13px;font-weight:700;color:var(--navy);margin-top:6px}

/* quote band */
.quote-band{top:583px;left:0;width:1200px;height:232px;background:var(--green);color:var(--white)}
.quote-band blockquote{top:84px;font-size:25px;font-weight:700;line-height:31px}
.quote-band cite{top:168px;font-style:normal;font-size:17px;color:#eaf3e3}

/* topics */
.topics-title{top:905px;font-size:26px;font-weight:700}
.topic{top:985px;width:220px}
.topic svg{display:block;margin-left:58px}
.topic h4{margin-top:18px;color:var(--green);font-size:17px;font-weight:700}
.topic ul{list-style:none;margin-top:9px;font-size:11.5px;line-height:20px;color:#333}
.topic a{display:block;margin-top:10px;font-size:11.5px;color:var(--green)}

/* founder */
.founder-photo{left:290px;top:1430px;width:118px;height:118px;border-radius:50%;background:linear-gradient(180deg,#d8c9a6,#c9a58a 55%,#3c6aa8)}
.founder-card{left:541px;top:1320px;width:430px;height:383px;background:var(--white);box-shadow:0 2px 8px rgba(0,0,0,.25);padding:56px 0 0 71px}
.founder-card h3{font-size:19px;font-weight:400}
.founder-card p{font-size:14px;line-height:20px;margin-top:20px;width:310px}
.founder-card p.role{margin-top:12px}
.founder-card .meet{display:block;margin-top:22px;font-size:17px;font-weight:900;color:var(--ink);text-decoration:none}

/* testimonial */
.testimonial{top:1772px;left:0;width:1200px;height:275px;background:var(--charcoal);color:var(--white)}
.testimonial h3{left:322px;top:50px;font-size:20px;font-weight:700}
.testimonial p{left:332px;top:90px;width:396px;font-size:14px;line-height:20px}
.testimonial cite{left:332px;top:186px;width:396px;text-align:right;font-style:normal;font-size:14px;font-weight:700}

/* blog */
.blog-title{top:2128px;font-size:19px;font-weight:700}
.post{top:2177px;width:268px;height:261px;color:var(--white);text-align:center;padding:0 8px}
.post .cat{margin-top:124px;font-size:12px;font-weight:900}
.post h4{margin:20px auto 0;width:222px;font-size:19px;line-height:20px;font-weight:700}
.post.steel{background:var(--steel)}
.post.green{background:var(--green-bright)}
.post.grey{background:var(--grey-card)}

/* signup */
.signup{top:2509px;left:0;width:1200px;height:223px;background:var(--steel-dark);color:var(--white)}
.signup h3{top:46px;font-size:20px;font-weight:700}
.signup p{top:85px;font-size:14px;color:#e4ebf2}
.field{top:132px;width:150px;height:29px;background:#f4f4f4;border:1px solid #c8c8c8;color:#9a9a9a;font-size:13px;padding:6px 12px}
.signup-btn{left:802px;top:132px;width:150px;height:29px;background:var(--green-bright);font-size:14px;font-weight:900;display:flex;align-items:center;justify-content:center}

/* research partners */
.partners-title{top:2778px;font-size:20px;font-weight:700}
.badge{top:2830px;height:90px;border-radius:4px}

/* call to action */
.cta{top:2958px;left:0;width:1200px;height:159px;background:var(--light)}
.cta h3{top:46px;font-size:23px;font-weight:700}
.btn-outline{left:519px;top:93px;width:162px;height:36px;border:2px solid var(--steel);color:var(--steel);font-size:14px;display:flex;align-items:center;justify-content:center;background:var(--white)}

/* footer */
.footer{top:3117px;left:0;width:1200px;height:300px;background:var(--navy);color:var(--white)}
.footer .brand{left:165px;top:56px;color:#8aa0b4}
.footer h5{font-size:15px;font-weight:700}
.footer .col{top:57px}
.footer .col p{font-size:12.5px;margin-top:8px}
.footer ul{list-style:none;font-size:11px;line-height:20px;margin-top:8px}
.socials{display:flex;gap:16px;margin-top:14px}
.socials span{width:14px;height:14px;border-radius:50%;background:#8aa0b4}
.copyright{top:3384px;left:0;width:1200px;text-align:center;font-size:9.5px;color:#c5d0da}
</style>
</head>
<body>

<header class="abs header">
  <div class="abs brand"><span>Loftwise</span><span class="dot"></span></div>
  <nav class="abs nav">
    <a class="active" href="#">HOME</a><a href="#">ABOUT</a><a href="#">SHOP</a><a href="#">BOOKS</a><a href="#">BLOG</a><a href="#">EXECUTIVE HEALTH</a><a href="#">CONTACT</a>
  </nav>
</header>

<section class="abs hero">
  <div class="abs hero-portrait" role="img" aria-label="Photo of a smiling bald bearded executive in a suit"></div>
  <div class="abs hero-growth" role="img" aria-label="Illustration of a rising growth arrow in warm orange"></div>
</section>
<h1 class="abs center hero-title">TAKE YOURSELF UP TO THE NEXT LEVEL</h1>
<p class="abs center hero-sub">MORE SUCCESS, HIGHER PRODUCTIVITY, BETTER HEALTH.</p>
<div class="abs btn-dark">SUBSCRIBE NOW</div>

<section class="abs promo">
  <div class="abs promo-col" style="left:140px">
    <h3>SHOP FOR HEALTHY EXECUTIVES</h3>
    <p>TOP SELECTED PRODUCTS FOR WORK AND HOME</p>
    <a href="#">BROWSE OUR SHOP</a>
  </div>
  <div class="abs promo-col" style="left:680px">
    <h3>GET FREE, EXCLUSIVE TIPS!</h3>
    <p>FROM EXERCISE TO EATING WELL, WE COVER IT ALL.</p>
    <a href="#">READ NOW</a>
  </div>
</section>

<section class="abs quote-band">
  <blockquote class="abs center">“Just by making small changes to your daily routine<br>you can significantly increase your productivity, health and business success”</blockquote>
  <cite class="abs center">Daniel Morrow – Founder of Loftwise.com</cite>
</section>

<h2 class="abs center topics-title">This site provides you with eye opening advice on:</h2>

<div class="abs topic" style="left:144px">
  <svg width="62" height="56" viewBox="0 0 62 56"><path d="M31 54 C10 38 0 28 0 16 A15 15 0 0 1 31 9 A15 15 0 0 1 62 16 C62 28 52 38 31 54Z" fill="var(--green)"/><polyline points="6,28 20,28 25,18 31,40 37,22 41,28 56,28" fill="none" stroke="#fff" stroke-width="3.5" stroke-linejoin="round"/></svg>
  <h4>Health &amp; Productivity</h4>
  <ul><li>Improve focus &amp; concentration</li><li>Boost productivity</li><li>Increase creativity &amp; energy levels</li><li>Reduce back pain &amp; headaches</li></ul>
  <a href="#">Learn More</a>
</div>
<div class="abs topic" style="left:397px">
  <svg width="62" height="56" viewBox="0 0 62 56"><path d="M6 50 C4 22 24 6 58 4 C58 34 42 52 14 48Z" fill="var(--green)"/><path d="M10 46 C22 34 34 24 46 16" stroke="#fff" stroke-width="3" fill="none" stroke-linecap="round"/></svg>
  <h4>Stress Reduction &amp; Sleep</h4>
  <ul><li>Reduce stress and anxiety</li><li>Gain a better sleep</li><li>Improve overall happiness</li><li>Fight Depression</li></ul>
  <a href="#">Learn More</a>
</div>
<div class="abs topic" style="left:661px">
  <svg width="62" height="56" viewBox="0 0 62 56"><ellipse cx="31" cy="40" rx="14" ry="12" fill="var(--green)"/><ellipse cx="22" cy="13" rx="6" ry="8" fill="var(--green)"/><ellipse cx="40" cy="13" rx="6" ry="8" fill="var(--green)"/><ellipse cx="8" cy="26" rx="6" ry="7" fill="var(--green)"/><ellipse cx="54" cy="26" rx="6" ry="7" fill="var(--green)"/></svg>
  <h4>Excercise</h4>
  <ul><li>Strengthen your immune system</li><li>Boost brain power</li><li>Reduce fatigue</li><li>Shape your body</li></ul>
  <a href="#">Learn More</a>
</div>
<div class="abs topic" style="left:898px">
  <svg width="62" height="56" viewBox="0 0 62 56"><g transform="rotate(-45 31 28)" fill="var(--green)"><rect x="27" y="2" width="8" height="52" rx="4"/><polygon points="31,20 4,34 4,40 31,32 58,40 58,34"/><polygon points="31,44 20,52 20,55 31,51 42,55 42,52"/></g></svg>
  <h4>Traveling</h4>
  <ul><li>Fight jet lag</li><li>Reduce travel fatigue</li><li>Sleep better when travelling</li><li>Exercise on the go</li></ul>
  <a href="#">Learn More</a>
</div>

<div class="abs founder-photo" role="img" aria-label="Portrait photo of the founder"></div>
<article class="abs founder-card">
  <h3>Who is Daniel?</h3>
  <p>A real executive, a certified corporate wellness coach and a personal trainer.</p>
  <p class="role">The Founder of Loft Wise</p>
  <a class="meet" href="#">MEET DANIEL</a>
</article>

<section class="abs testimonial">
  <h3 class="abs">Hear what other Executives said about Daniel:</h3>
  <p class="abs">“In the past I thought that my success only depends on<br>working harder and harder. Loftwise.com made me aware<br>that I need to work smarter and that my success depends not<br>only on my brain but also on my body.”</p>
  <cite class="abs">- Luca Bernardi | VP, Italy</cite>
</section>

<h2 class="abs center blog-title">Read the latest tips on Healthy Productivity</h2>
<article class="abs post steel" style="left:120px"><div class="cat">STRESS REDUCTION &amp; MENTAL HEALTH</div><h4>Why Is Meditation Good for You and Your Business?</h4></article>
<article class="abs post green" style="left:466px"><div class="cat">GENERAL HEALTH</div><h4>Effects of Blue Light: Should Executives Be Worried?</h4></article>
<article class="abs post grey" style="left:812px"><div class="cat">HEALTHY SLEEP</div><h4>The Real Reason Why You Are Struggling to Sleep at Night</h4></article>

<section class="abs signup">
  <h3 class="abs center">Join the movement.</h3>
  <p class="abs center">Get free, exclusive tips in your inbox to become a healthy manager.</p>
  <div class="abs field" style="left:248px">First Name</div>
  <div class="abs field" style="left:429px">Last Name</div>
  <div class="abs field" style="left:610px">Email</div>
  <div class="abs signup-btn">Signup</div>
</section>

<h2 class="abs center partners-title">THE WEBSITE CONTENT IS INSPIRED BY THE RESEARCH AND PUBLICATIONS OF:</h2>
<div class="abs badge" style="left:197px;width:157px;background:#e6e6e6"></div>
<div class="abs badge" style="left:392px;width:118px;background:#f2f2f2"></div>
<div class="abs badge" style="left:548px;width:150px;background:#f4eded"></div>
<div class="abs badge" style="left:771px;top:2837px;width:63px;height:63px;background:#1f6fb4"></div>
<div class="abs badge" style="left:900px;width:150px;background:#f3f4f7"></div>

<section class="abs cta">
  <h3 class="abs center">START YOUR PATH TO HEALTH &amp; SUCCESS NOW!</h3>
  <div class="abs btn-outline">SUBSCRIBE NOW</div>
</section>

<footer class="abs footer">
  <div class="abs brand"><span>Loftwise</span><span class="dot"></span></div>
  <div class="abs col" style="left:473px;top:62px"><h5>CONTACT</h5><p>contact@loftwise.com</p></div>
  <div class="abs col" style="left:710px"><h5>QUICK LINKS</h5>
    <ul><li>Home</li><li>About</li><li>Shop</li><li>Books</li><li>Blog</li><li>Executive Health</li><li>Contact</li></ul></div>
  <div class="abs col" style="left:910px;top:55px"><h5>CONNECT</h5><div class="socials"><span></span><span></span><span></span><span></span></div></div>
</footer>
<p class="abs copyright">(c) Loftwise. All rights reserved</p>

</body>
</html>
```